We are a music company that specializes in Music Mixing and Mastering. We also do vocal recording and create instrumentals for various artists. Our website is 731kv.com

Target Market(s)

Musicians, Record labels, rappers, and singers

Industry/Entity Type

Artists

Contact Information for Business Card

731KV
Industry Standard Mixing & Mastering
(484) 317-2095
sales@731kv.com
731kv.com

Requirements
Must have
• contact info and twitter (@731KV)

```html
<!DOCTYPE html>
<html lang="en">
<head>
<meta charset="utf-8">
<title>731KV — Business Card</title>
<link rel="stylesheet" href="https://fonts.googleapis.com/css2?family=Questrial&display=swap">
<style>
  :root {
    --card-bg: #29261f;
    --backdrop-letters: #322f27;
    --accent: #c4532f;
    --tagline: #8b8880;
    --contact: #6f6c64;
  }
  html, body {
    margin: 0;
    padding: 0;
    width: 1200px;
    height: 709px;
    overflow: hidden;
    background: var(--card-bg);
  }
  .card {
    position: relative;
    width: 1200px;
    height: 709px;
    background: var(--card-bg);
    overflow: hidden;
    font-family: "Questrial", "Helvetica Neue", Arial, sans-serif;
  }
  .backdrop-name {
    position: absolute;
    left: -10px;
    top: -40px;
    margin: 0;
    font-size: 640px;
    line-height: 1;
    letter-spacing: -20px;
    color: var(--backdrop-letters);
    white-space: nowrap;
    user-select: none;
  }
  .brand-name {
    position: absolute;
    left: 0;
    right: 0;
    top: 195px;
    margin: 0;
    text-align: center;
    font-size: 150px;
    line-height: 1;
    font-weight: 400;
    letter-spacing: 2px;
    color: var(--accent);
  }
  .tagline {
    position: absolute;
    left: 0;
    right: 0;
    top: 380px;
    margin: 0;
    text-align: center;
    font-size: 38px;
    line-height: 48px;
    letter-spacing: 6px;
    color: var(--tagline);
  }
  .tagline .amp { color: var(--accent); }
  .contact-line {
    position: absolute;
    left: 0;
    right: 0;
    top: 617px;
    margin: 0;
    text-align: center;
    font-size: 30px;
    letter-spacing: 1.5px;
    color: var(--contact);
    white-space: nowrap;
  }
  .contact-line .divider {
    color: var(--accent);
    margin: 0 10px;
  }
</style>
</head>
<body>
  <main class="card">
    <p class="backdrop-name" aria-hidden="true">731KV</p>
    <h1 class="brand-name">731KV</h1>
    <p class="tagline">Industry Standard<br>Mixing <span class="amp">&amp;</span> Mastering</p>
    <p class="contact-line">
      <span class="phone">(484) 317-2095</span><span class="divider">|</span><span class="email">sales@731kv.com</span><span class="divider">|</span><span class="website">731kv.com</span><span class="divider">|</span><span class="handle">@731KV</span>
    </p>
  </main>
</body>
</html>
```